Sticker for Scrap Metal Bin that is placed at customers premises

During the course of our operation, Scrap Metal Bin are place at our customer site for them to dispose scrap metal into the Bin.

Would like to have a sticker for us to paste on the bin.

All scrap bin will be blue color. Attached sample of current sticker on a scrap bin.

Would like one that is clean, simple and eye catching also that the font is much visible unlike the current one that is cramp and small.

Target Market(s)

Businesses

Font styles to use
Serif

Requirements
Must have
• 1) Company Name and Logo
• 2) Contact Details : 9312 4057 / 6248 3915
• 3) Website: www.choklimtat.com

```html
<!DOCTYPE html>
<html lang="en">
<head>
<meta charset="utf-8">
<title>Scrap Metal Bin Sticker</title>
<link href="https://fonts.googleapis.com/css2?family=Overpass:wght@600;700&display=swap" rel="stylesheet">
<style>
  :root {
    --ink: #000000;
    --paper: #ffffff;
    --gold: #c99a2e;
    --dark-text: #111111;
  }
  html, body {
    margin: 0;
    padding: 0;
    overflow: hidden;
    background: var(--paper);
  }
  .sticker {
    position: relative;
    width: 1200px;
    height: 966px;
    background: var(--paper);
    font-family: "Overpass", Arial, sans-serif;
    overflow: hidden;
  }
  .sign-panel {
    position: absolute;
    left: 0;
    top: 0;
    width: 1200px;
    height: 826px;
    background: var(--ink);
  }
  .sign-frame {
    position: absolute;
    left: 46px;
    top: 32px;
    width: 1108px;
    height: 763px;
    box-sizing: border-box;
    border: 13px solid var(--paper);
  }
  .sign-words {
    position: absolute;
    left: 0;
    top: 0;
  }
  .sign-words text {
    font-family: "Overpass", Arial, sans-serif;
    font-weight: 600;
    fill: var(--paper);
  }
  .brand {
    position: absolute;
    left: 18px;
    top: 839px;
    width: 224px;
    color: var(--gold);
    font-weight: 700;
  }
  .brand-mark {
    display: block;
    width: 60px;
    height: 60px;
    margin-left: 79px;
    box-sizing: border-box;
    border: 3px solid var(--gold);
  }
  .brand-name {
    margin: 12px 0 0;
    font-size: 24px;
    line-height: 1;
    letter-spacing: 1px;
    white-space: nowrap;
  }
  .brand-tag {
    margin: 2px 0 0;
    font-size: 15px;
    line-height: 1;
    letter-spacing: 1px;
    text-align: right;
  }
  .contact {
    position: absolute;
    left: 890px;
    top: 852px;
    margin: 0;
    padding: 0;
    list-style: none;
    color: var(--dark-text);
    font-weight: 700;
    font-size: 24px;
    line-height: 1;
  }
  .contact-item {
    display: flex;
    align-items: center;
    height: 32px;
    white-space: nowrap;
  }
  .contact-item + .contact-item {
    margin-top: 28px;
  }
  .contact-icon {
    flex: none;
    margin-right: 13px;
  }
</style>
</head>
<body>
<main class="sticker">
  <section class="sign-panel">
    <div class="sign-frame"></div>
    <svg class="sign-words" width="1200" height="826" viewBox="0 0 1200 826" aria-label="Scrap Metal">
      <text x="82" y="386" font-size="330" textLength="1036" lengthAdjust="spacingAndGlyphs">SCRAP</text>
      <text x="96" y="675" font-size="322" textLength="1002" lengthAdjust="spacingAndGlyphs">METAL</text>
    </svg>
  </section>

  <div class="brand">
    <span class="brand-mark"></span>
    <p class="brand-name">CHOK LIM TAT</p>
    <p class="brand-tag">RECYCLING</p>
  </div>

  <ul class="contact">
    <li class="contact-item">
      <svg class="contact-icon" width="20" height="30" viewBox="0 0 20 30" aria-hidden="true">
        <rect x="2" y="1.5" width="16" height="27" rx="3" fill="none" stroke="#111" stroke-width="3"/>
        <line x1="7.5" y1="24" x2="12.5" y2="24" stroke="#111" stroke-width="2"/>
      </svg>
      <span>9312 4057 / 6248 3915</span>
    </li>
    <li class="contact-item">
      <svg class="contact-icon" width="30" height="30" viewBox="0 0 30 30" aria-hidden="true">
        <circle cx="15" cy="15" r="13.5" fill="#111"/>
        <g fill="none" stroke="#fff" stroke-width="1.8">
          <ellipse cx="15" cy="15" rx="5.5" ry="13.5"/>
          <line x1="15" y1="1.5" x2="15" y2="28.5"/>
          <line x1="1.5" y1="15" x2="28.5" y2="15"/>
          <path d="M4 8.5 H26 M4 21.5 H26"/>
        </g>
      </svg>
      <span>www.choklimtat.com</span>
    </li>
  </ul>
</main>
</body>
</html>
```